Kaffeerösterei sucht Etiketten-Design
- schnelle Ausführung - mein Geschmack voll getroffen - unkompliziert und Kunden orientiert bei der Ausführung
Zielgruppe
Kaffeerösterei für die edelsten und teuersten Rohkaffees.
Meine Kunden sind Kaffee Geniesser.
Aufgabenstellung
Transparente Aufkleber für eine Schiefertafel im Format 22.5 cm x 15.5 cm.
Im Hand-Lettering Stil.
5 Schiefertafeln sind gewünscht.
Tafel 1
Kostenlos zur Degustation
Espresso
Café Crème 3.--
Americano 3.--
Filter Kaffee 3.--
Tafel 2
Kaffee & Milch
Cappuccino 4.--
Café Latte 4.--
Flat White 4.--
Latte Macchiato 4.--
Latte Macchiato mit Aroma 5.--
Kaffee & Hafermilch + 1.--
Tafel 3
Crepes
Pikant
- Pizza Crepes 7.--
- Flammkuchen Crepes 7.--
Süss
- Schoggi Crepes 6.--
- Apfelmus & Zimtzucker 6.--
Tafel 4
Kaffee & Schnaps
- Original Entlebucher Schwarzes 7.--
- Espresso Coretto 5.00
- Schwarzes mit Rahmhaube 8.--
Tafel 5
Schokolade & Milch
- heisse Schoggi 5.--
- heisse Schoggi mit Rahmhaube 6.--
- heisse Schoggi mit Espresso 6.--
- Schokolade & Hafermilch +1.--
Als Idee, was mir gefallen könnte:
https://www.bildsammlung.example/pin/104857392018374655/
https://de.grafikhort.example/vektorkunst/4418203-set-kaffeekarte-mit-tassen-kaffeegetranken-im-vintage-stil-stilisierte-zeichnung-mit-kreide-auf-tafel-schriftzug-sample-drinks
https://www.fotolager.example/stockfoto-heisser-kakao-bar-warm-hier-oben-hand-tafel-caf-schild-an-tafel-hintergrund-mit-farbe-kreide-schriftzug-werbung-fur-heisse-d-583021746.html

```html
<!DOCTYPE html>
<html lang="de">
<head>
<meta charset="utf-8">
<title>Kostenlos zur Degustation – Espresso</title>
<link rel="stylesheet" href="https://fonts.googleapis.com/css2?family=Amatic+SC:wght@700&family=Kaushan+Script&display=swap">
<style>
  :root {
    --paper: #ffffff;
    --slate: #1d1d1b;
    --chalk: #ffffff;
    --cream: #fdecd3;
    --honey: #fbcf79;
  }
  html, body {
    margin: 0;
    padding: 0;
    width: 1200px;
    height: 869px;
    overflow: hidden;
    background: var(--paper);
  }
  .board {
    position: absolute;
    left: 65px;
    top: 70px;
    width: 1063px;
    height: 732px;
    background: var(--slate);
  }
  .tagline {
    position: absolute;
    left: 0;
    width: 100%;
    top: 83px;
    margin: 0;
    text-align: center;
    font-family: "Amatic SC", sans-serif;
    font-weight: 700;
    font-size: 74px;
    line-height: 1;
    letter-spacing: 7px;
    color: var(--honey);
  }
  .title {
    position: absolute;
    left: 0;
    width: 100%;
    top: 156px;
    margin: 0;
    text-align: center;
    font-family: "Kaushan Script", cursive;
    font-weight: 400;
    font-size: 100px;
    line-height: 1.2;
    color: var(--chalk);
  }
  .flourish {
    position: absolute;
    top: 210px;
    width: 78px;
    height: 41px;
    border-radius: 20px;
    background: var(--cream);
    opacity: 0.85;
  }
  .flourish--left { left: 232px; }
  .flourish--right { left: 753px; }
  .menu {
    position: absolute;
    left: 0;
    top: 357px;
    width: 100%;
    margin: 0;
    padding: 0;
    list-style: none;
  }
  .menu__item {
    position: relative;
    height: 87px;
  }
  .menu__name {
    position: absolute;
    right: 436px;
    top: 0;
    font-family: "Amatic SC", sans-serif;
    font-weight: 700;
    font-size: 73px;
    line-height: 1;
    letter-spacing: 8px;
    color: var(--chalk);
    white-space: nowrap;
  }
  .menu__price {
    position: absolute;
    left: 690px;
    top: 0;
    font-family: "Amatic SC", sans-serif;
    font-weight: 700;
    font-size: 73px;
    line-height: 1;
    letter-spacing: 6px;
    color: var(--cream);
    white-space: nowrap;
  }
  .underline {
    position: absolute;
    left: 358px;
    top: 722px;
  }
</style>
</head>
<body>
  <main class="board" aria-label="Schiefertafel Degustation">
    <h2 class="tagline">Kostenlos zur Degustation</h2>
    <div class="flourish flourish--left" role="img" aria-label="Geschwungenes Schmuckornament links"></div>
    <h1 class="title">Espresso</h1>
    <div class="flourish flourish--right" role="img" aria-label="Geschwungenes Schmuckornament rechts"></div>

    <ul class="menu">
      <li class="menu__item"><span class="menu__name">Café Crème</span><span class="menu__price">3,–</span></li>
      <li class="menu__item"><span class="menu__name">Americano</span><span class="menu__price">3,–</span></li>
      <li class="menu__item"><span class="menu__name">Filter Kaffee</span><span class="menu__price">3,–</span></li>
    </ul>
  </main>

  <svg class="underline" width="476" height="20" viewBox="0 0 476 20" aria-hidden="true">
    <path d="M2 8 C 60 3, 140 1, 260 1 C 350 1, 415 5, 474 12 C 462 15, 432 14, 392 13 C 315 11, 200 10, 90 12 C 50 13, 15 16, 2 8 Z" fill="var(--honey)"/>
  </svg>
</body>
</html>
```